New Business Card Design for Business Consulting Business

We need a business card design that reflects the simplicity of our business. We partner with our clients to help them deliver change. We are a different kind of business consulting group. We don't just provide you with the theory. We provide you with the leadership and capability to execute change.

Vonduro is a professional services organisation that partners with their clients to lead the execution of strategic process and system improvement initiatives. Vonduro combines hands on delivery with coaching in best practice methodologies and approaches to build their clients capabilities to ensure their ongoing success in project implementations. Vonduro offers business advisory services in Project Management, Business Process Management, Change Management and Business Analytics.

Reason: Hi Designers, Thanks for all of your great designs. There are some really creative and cool ideas. Everyone is really capturing the essence of my business Vonduro. I am extending the deadline for the business card design by 6 days as I need to consult my Marketing colleague who won't be back in Australia until Wednesday. I would like to sit down with them and review all of the best designs. The key themes of the things I have really liked on my first review are: 1) Capturing the company website on the back of the card. 2) Including the company logo on the back of the card too. 3) Including the types of services on the back of the card that the company offers - Project Management - Business Process Management - Change Management - Business Analytics 4) Utilising some images on the back of the card Just so everyone knows the colour palette for the Vonduro company logo is: R: 0 G: 86 B: 162 or C: 97% M: 73% Y: 4% K: 0% Thanks Gareth

Hi Designers,

Thanks for all of your submissions to date.  I am working through each design and will provide feedback on all the great work.

One thing I would like to ask is if you could submit a version that has my academic credentials under or after my name.  I am not a big fan of doing this but as I am in business consulting it does seem to be quite common.

I hold a Bachelor of Commerce (BCom) and a Master of Business Administration (MBA)

Thanks

Gareth

Hi Designers,

Thanks for all of your fantastic designs.  There are some really great designs here for my business.  I am still in the process of reviewing designs and should have this completed by tomorrow.  Some of the things I have learnt from this round of designs are:

1) I prefer to have the card without my academic qualifications

2) I really like cards that have a blue back

3) I prefer to have my name and title either left or right of centre

I hope this helps and I will endeavour to get through all of the designs tomorrow

Cheers

Gareth

Target Market(s)

We target large corporate organisations

Industry/Entity Type

Leadership

Requirements
Must have
• Must have the following business details

Gareth Pilling - Director
Address: Level 7, 82 Harlow Street, Melbourne, Australia, 3000
Phone: +61 3 527 840 213
Fax: +61 3 9214 5037
Email: gareth.pilling@vonduro-example.com.au
LinkedIn: au.linkedin.com/in/garethjpilling/
Twiiter: @garethjpilling
Website: www.vonduro-example.com.au

```html
<!DOCTYPE html>
<html lang="en">
<head>
<meta charset="utf-8">
<title>Vonduro Business Card</title>
<link href="https://fonts.googleapis.com/css2?family=Exo+2:wght@300;400&display=swap" rel="stylesheet">
<style>
  :root {
    --brand-blue: #0056a2;
    --ink-grey: #444548;
    --paper: #ffffff;
    --backdrop: #e4e5e7;
    --soft-white: #eaf1f9;
  }
  * { box-sizing: border-box; margin: 0; padding: 0; }
  html, body {
    width: 1200px; height: 985px; overflow: hidden;
    background: var(--backdrop);
    font-family: "Exo 2", sans-serif;
  }
  .stage { position: relative; width: 1200px; height: 985px; }
  .card {
    position: absolute; left: 320px; width: 560px; height: 320px;
    border-radius: 22px; overflow: hidden;
    box-shadow: 0 6px 18px rgba(0,0,0,0.18);
  }
  .card-back { top: 140px; background: var(--brand-blue); }
  .card-front { top: 520px; background: var(--paper); }

  .wordmark { font-weight: 300; letter-spacing: 1px; line-height: 1; }
  .card-back .wordmark {
    position: absolute; left: 150px; top: 110px;
    font-size: 72px; color: var(--paper);
  }
  .legal-suffix {
    display: block; font-size: 10px; letter-spacing: 0.5px;
    text-align: right; margin-top: 4px; font-weight: 300;
  }
  .card-back .legal-suffix { color: var(--paper); }

  .front-shapes { position: absolute; inset: 0; }
  .card-front .wordmark {
    position: absolute; left: 28px; top: 26px;
    font-size: 52px; color: var(--brand-blue);
  }
  .card-front .legal-suffix { color: var(--brand-blue); font-size: 8px; }

  .person {
    position: absolute; left: 30px; top: 176px; color: var(--brand-blue);
    white-space: nowrap;
  }
  .person-name { font-size: 19px; font-weight: 300; }
  .person-creds {
    font-size: 10px; color: var(--ink-grey); margin-left: 4px;
    padding-left: 4px; border-left: 1.5px solid var(--ink-grey);
  }
  .person-title { font-size: 13px; font-weight: 300; margin-top: 1px; }

  .address {
    position: absolute; right: 24px; top: 90px; width: 200px;
    color: var(--paper); font-size: 14px; font-weight: 300;
    line-height: 1.25; white-space: nowrap;
  }
  .contacts {
    position: absolute; right: 22px; top: 168px;
    list-style: none; color: var(--soft-white);
    font-size: 12px; font-weight: 300;
  }
  .contacts li {
    display: flex; justify-content: flex-end; align-items: center;
    height: 21px; gap: 8px; white-space: nowrap;
  }
  .contact-icon {
    width: 17px; height: 15px; border-radius: 3px;
    background: var(--paper); color: var(--brand-blue);
    font-size: 9px; font-weight: 400;
    display: flex; align-items: center; justify-content: center;
  }
  .contact-icon svg { width: 10px; height: 10px; }
  .contact-icon.plain { background: transparent; border: 1.5px solid var(--paper); }
</style>
</head>
<body>
<main class="stage">

  <section class="card card-back" aria-label="Card back">
    <div class="wordmark">Vonduro<span class="legal-suffix">Pty Ltd</span></div>
  </section>

  <section class="card card-front" aria-label="Card front">
    <svg class="front-shapes" viewBox="0 0 560 320" preserveAspectRatio="none" aria-hidden="true">
      <path d="M400 0 Q250 100 228 320 L244 320 Q268 100 430 0 Z" fill="var(--ink-grey)"/>
      <path d="M430 0 Q268 100 244 320 L560 320 L560 0 Z" fill="var(--brand-blue)"/>
    </svg>

    <div class="wordmark">Vonduro<span class="legal-suffix">Pty Ltd</span></div>

    <div class="person">
      <div><span class="person-name">Gareth Pilling</span><span class="person-creds">BCom, MBA</span></div>
      <div class="person-title">Director</div>
    </div>

    <p class="address">Level 7, 82 Harlow Street,<br>Melbourne, Australia, 3000</p>

    <ul class="contacts">
      <li>+61 3 527 840 213
        <span class="contact-icon"><svg viewBox="0 0 10 10"><path d="M2 1 L4 1 L4.6 3 L3.5 3.8 Q4.5 6 6.2 6.5 L7 5.4 L9 6 L9 8 Q8.5 9 7 9 Q1.5 8 1 2.5 Q1 1 2 1 Z" fill="currentColor"/></svg></span></li>
      <li>+61 3 9214 5037 <span class="contact-icon">Fx</span></li>
      <li>gareth.pilling@vonduro-example.com.au <span class="contact-icon">@</span></li>
      <li>www.vonduro-example.com.au
        <span class="contact-icon"><svg viewBox="0 0 10 10" fill="none" stroke="currentColor" stroke-width="1"><circle cx="5" cy="5" r="4"/><ellipse cx="5" cy="5" rx="1.8" ry="4"/><path d="M1 5 H9"/></svg></span></li>
      <li>au.linkedin.com/in/garethjpilling/ <span class="contact-icon plain"></span></li>
      <li>@garethjpilling <span class="contact-icon plain"></span></li>
    </ul>
  </section>

</main>
</body>
</html>
```